innovative investment real estate sales firm

We are a uniquely collabrative firm that seeks to bring a conultative approach to uncovering hidden opportunities for our clients, our website needs to convey our client focused approach. Our firm specializes in the sale of apartment properties in Southern California. We have a team of researchers, transaction coordinators and marketing personal to support our geographically specialized advisers. We need a website that introduces clients to our unique way of better helping them achieve their investment goals.

Target Market(s)

High net worth individuals and families

Industry/Entity Type

Real Estate Agent

Font styles to use
Other font styles liked:
• please use font provided

Requirements
Must have
• Stories of our recent projects
• Features on our people
• email capture for viewing inventory
• content that showcases our unique consultative approach that uncovers unrealized opportunities

```html
<!DOCTYPE html>
<html lang="en">
<head>
<meta charset="utf-8">
<title>Meridian Advisers – Multifamily Properties</title>
<link rel="stylesheet" href="https://fonts.googleapis.com/css2?family=Montserrat:wght@400;500;600;700&family=Open+Sans:ital,wght@0,400;0,600;0,700;1,400&display=swap">
<style>
:root{
  --teal:#1ba8c4;
  --teal-dark:#1390aa;
  --green:#9cc83a;
  --ink:#2b2e33;
  --slate:#4b5057;
  --text:#555a60;
  --light:#f2f3f4;
  --white:#ffffff;
  --rule:#d7dadd;
}
*{box-sizing:border-box;margin:0;padding:0}
html,body{width:1200px;height:3488px;overflow:hidden}
body{font-family:"Open Sans",Arial,sans-serif;color:var(--text);background:var(--white);position:relative}

/* header */
.topbar{position:absolute;top:0;left:0;width:1200px;height:46px}
.topbar::before{content:"";position:absolute;right:0;top:0;width:760px;height:34px;background:var(--teal)}
.topbar .contact{position:absolute;right:36px;top:8px;color:var(--white);font-size:13px;display:flex;gap:22px;align-items:center}
.topbar .contact span{display:flex;gap:6px;align-items:center}
.brand{position:absolute;left:44px;top:44px;display:flex;align-items:center;gap:14px}
.brand .mark{width:46px;height:46px;background:var(--teal)}
.brand .name{font-family:"Montserrat",Arial,sans-serif;font-weight:600;font-size:26px;letter-spacing:2px;color:var(--ink)}
.nav{position:absolute;right:36px;top:100px;display:flex;gap:30px;align-items:center;font-family:"Montserrat",Arial,sans-serif;font-weight:600;font-size:14px;color:var(--ink);letter-spacing:.5px}
.nav .home{width:18px;height:16px}

/* hero */
.hero{position:absolute;top:158px;left:0;width:1200px;height:558px;
  background:linear-gradient(180deg,#5b5f7a 0%,#b9867e 22%,#6d6874 40%,#3a3f47 65%,#1f2228 100%)}
.hero .arrow{position:absolute;top:256px;width:40px;height:44px;background:var(--teal);display:flex;align-items:center;justify-content:center}
.hero .arrow.left{left:10px}
.hero .arrow.right{right:10px}
.welcome{position:absolute;top:716px;left:0;width:1200px;height:156px;background:#24272b;text-align:center;color:var(--white)}
.welcome h1{font-family:"Montserrat",Arial,sans-serif;font-weight:600;font-size:29px;letter-spacing:1.5px;margin-top:36px}
.welcome h1 em{font-style:normal;color:var(--teal)}
.welcome p{font-size:16px;line-height:24px;margin:10px auto 0;width:1060px}

/* shared headings */
.sec-title{display:flex;align-items:center;justify-content:center;gap:18px;font-family:"Montserrat",Arial,sans-serif;font-weight:600;font-size:26px;color:var(--ink);letter-spacing:1px}
.sec-title .rule{width:70px;height:1px;background:var(--rule)}
.sec-title .mark{width:34px;height:34px;background:var(--teal)}
.sec-title em{font-style:normal;color:var(--green)}
.on-teal .sec-title{color:var(--white)}
.on-teal .sec-title .rule{background:rgba(255,255,255,.6)}
.on-teal .sec-title .mark{background:var(--white)}
.btn{display:inline-block;border:2px solid var(--green);border-radius:4px;font-family:"Montserrat",Arial,sans-serif;font-weight:700;font-size:14px;color:var(--ink);letter-spacing:.5px;text-align:center}

/* about */
.about{position:absolute;top:872px;left:0;width:1200px;height:372px;text-align:center}
.about .sec-title{margin-top:48px}
.about p{width:1040px;margin:38px auto 0;font-size:14.5px;line-height:22.5px}
.about .btn{margin-top:26px;width:190px;height:40px;line-height:36px}

/* people */
.people{position:absolute;top:1244px;left:0;width:1200px;height:512px;
  background:linear-gradient(135deg,#3dbad1 0%,#22a9c4 45%,#1698b5 100%)}
.people .sec-title{margin-top:60px}
.people .carousel-arrow{position:absolute;top:236px;width:30px;height:30px}
.people .carousel-arrow.left{left:64px}
.people .carousel-arrow.right{right:64px}
.team{position:absolute;top:137px;left:140px;width:920px;display:flex;justify-content:space-between}
.member{width:220px;text-align:center;color:var(--white)}
.member .portrait{width:212px;height:212px;margin:0 auto;border-radius:50%;border:3px solid rgba(255,255,255,.55);padding:10px}
.member .portrait div{width:100%;height:100%;border-radius:50%;background:radial-gradient(circle at 50% 40%,#e9ecef 0%,#c9ced4 70%,#aab1b8 100%)}
.member h3{font-family:"Open Sans",Arial,sans-serif;font-weight:700;font-size:16px;margin-top:18px}
.member p{font-size:15px;font-weight:600;margin-top:1px}
.member .social{display:flex;justify-content:center;gap:9px;margin-top:18px;align-items:center}
.member .social i{display:block;width:12px;height:12px;border-radius:50%;background:rgba(255,255,255,.85)}

/* services */
.services{position:absolute;top:1756px;left:0;width:1200px;height:379px}
.services .sec-title{margin-top:56px}
.service{position:absolute;top:140px;width:480px}
.service.one{left:56px}
.service.two{left:630px}
.service .icon{position:absolute;left:0;top:6px;width:118px;height:118px;border-radius:50%;border:3px solid var(--teal);display:flex;align-items:center;justify-content:center}
.service .body{margin-left:130px}
.service h3{font-family:"Open Sans",Arial,sans-serif;font-weight:700;font-size:17px;color:var(--teal)}
.service p{font-size:14.5px;line-height:20.5px;color:var(--ink);margin-top:2px}
.service .btn{margin-top:20px;width:190px;height:38px;line-height:34px}

/* approach */
.approach{position:absolute;top:2135px;left:0;width:1200px;height:498px;
  background:linear-gradient(180deg,#2fb4cd 0%,#1ea8c3 60%,#1b9fbb 100%)}
.approach .sec-title{margin-top:60px}
.approach svg{position:absolute;left:0;top:0}
.step{position:absolute;text-align:center;color:var(--ink);font-size:13.5px;line-height:17.5px}
.step h3{font-family:"Montserrat",Arial,sans-serif;font-weight:600;font-size:15px;color:var(--teal);letter-spacing:.5px;margin-bottom:2px}

/* testimonials */
.testimonials{position:absolute;top:2633px;left:0;width:1200px;height:433px}
.testimonials .sec-title{margin-top:56px}
.quote{position:absolute;left:256px;top:136px;width:693px;height:142px;border:1px solid var(--rule);border-radius:6px;background:#fafafa;padding:22px 22px 0 56px;font-size:14px;line-height:22px;color:var(--ink)}
.quote .q{position:absolute;font-family:Georgia,serif;font-size:40px;font-weight:700;color:var(--ink);line-height:1}
.quote .q.open{left:18px;top:16px}
.quote .close{font-family:Georgia,serif;font-size:30px;font-weight:700;line-height:0;vertical-align:-8px;margin-left:4px}
.quote .tail{position:absolute;left:28px;bottom:-13px;width:24px;height:24px;background:#fafafa;border-right:1px solid var(--rule);border-bottom:1px solid var(--rule);transform:rotate(45deg)}
.testimonials .author{position:absolute;left:256px;top:300px;font-style:italic;font-size:15px;color:var(--ink)}
.dots{position:absolute;top:346px;left:0;width:1200px;display:flex;justify-content:center;gap:6px}
.dots i{width:11px;height:11px;border-radius:50%;border:1px solid var(--slate)}
.dots i.on{background:var(--teal);border-color:var(--teal)}

/* footer */
.footer{position:absolute;top:3066px;left:0;width:1200px;height:365px;background:var(--light)}
.footer .brand{position:absolute;left:0;width:1200px;top:44px;justify-content:center}
.footer .brand .mark{width:54px;height:54px}
.footer .brand .name{font-size:28px}
.fcol{position:absolute;top:151px}
.fcol h4{font-family:"Montserrat",Arial,sans-serif;font-weight:700;font-size:14px;color:var(--teal);letter-spacing:.5px;padding-bottom:10px;border-bottom:1px solid var(--rule);width:170px}
.fcol ul{list-style:none;margin-top:20px;font-size:12.5px;line-height:15.5px;color:var(--ink)}
.fcol .line{display:flex;gap:8px;font-size:12.5px;line-height:15.5px;color:var(--ink);margin-top:14px}
.fcol .line svg{flex:none}
.signup{display:flex;margin-top:24px}
.signup .field{width:168px;height:36px;border:1px solid var(--teal);background:var(--white);font-size:13px;color:var(--ink);padding:9px 10px}
.signup .go{width:93px;height:36px;background:var(--teal);color:var(--white);font-family:"Montserrat",Arial,sans-serif;font-weight:700;font-size:13px;text-align:center;line-height:36px}
.copyright{position:absolute;top:3431px;left:0;width:1200px;height:57px;background:var(--teal);color:var(--white);text-align:center;font-size:11.5px;font-weight:600;line-height:57px;letter-spacing:.5px}
</style>
</head>
<body>

<header>
  <div class="topbar">
    <div class="contact">
      <span><svg width="12" height="12" viewBox="0 0 12 12"><path d="M2.5 1l2 2-1 1.5a7 7 0 0 0 4 4L9 7.5l2 2L9.5 11C5 11 1 7 1 2.5z" fill="#fff"/></svg>+1 (555) 014 2290</span>
      <span><svg width="14" height="10" viewBox="0 0 14 10"><rect x=".5" y=".5" width="13" height="9" fill="none" stroke="#fff"/><path d="M.5.5L7 6l6.5-5.5" fill="none" stroke="#fff"/></svg>hello@meridianadvisers.example</span>
    </div>
  </div>
  <div class="brand"><div class="mark"></div><div class="name">MERIDIAN ADVISERS</div></div>
  <nav class="nav">
    <svg class="home" viewBox="0 0 18 16"><path d="M9 1L1 8h2.5v7h4v-4.5h3V15h4V8H17z" fill="var(--teal)"/></svg>
    <span>ABOUT</span><span>OUR PEOPLE</span><span>SERVICES</span><span>APPROACH</span><span>TESTIMONIALS</span><span>CONTACT</span>
  </nav>
</header>

<section class="hero" role="img" aria-label="Dusk photograph of a modern multifamily apartment row with palm trees along a street">
  <div class="arrow left"><svg width="12" height="18" viewBox="0 0 12 18"><path d="M10 2L3 9l7 7" fill="none" stroke="#fff" stroke-width="3"/></svg></div>
  <div class="arrow right"><svg width="12" height="18" viewBox="0 0 12 18"><path d="M2 2l7 7-7 7" fill="none" stroke="#fff" stroke-width="3"/></svg></div>
</section>
<section class="welcome">
  <h1>WELCOME TO <em>MERIDIAN ADVISERS</em></h1>
  <p>Our firm specializes in the sale of apartment properties in Southern California. We have a team of researchers, transaction coordinators and marketing personal to support our geographically specialized advisers.</p>
</section>

<section class="about">
  <h2 class="sec-title"><span class="rule"></span><span class="mark"></span><span>ABOUT <em>US</em></span><span class="rule"></span></h2>
  <p>Lorem ipsum dolor sit amet, consectetuer adipiscing elit, sed diam nonummy nibh euismod tincidunt ut laoreet dolore magna aliquam erat volutpat. Ut wisi enim ad minim veniam, quis nostrud exerci tation ullamcorper suscipit lobortis nisl ut aliquip ex ea commodo consequat. Duis autem vel eum iriure dolor in hendrerit in vulputate velit esse molestie consequat, vel illum dolore eu feugiat nulla facilisis at vero eros et accumsan et iusto odio dignissim qui blandit praesent luptatum zzril delenit augue duis dolore te feugait nulla facilisi. Nam liber tempor cum soluta nobis eleifend option congue nihil imperdiet doming id quod mazim placerat facer possim assum.</p>
  <span class="btn">LEARN MORE</span>
</section>

<section class="people on-teal" role="group" aria-label="Our people">
  <h2 class="sec-title"><span class="rule"></span><span class="mark"></span><span>OUR PEOPLE</span><span class="rule"></span></h2>
  <svg class="carousel-arrow left" viewBox="0 0 30 30"><path d="M20 3L8 15l12 12" fill="none" stroke="#fff" stroke-width="4"/></svg>
  <svg class="carousel-arrow right" viewBox="0 0 30 30"><path d="M10 3l12 12-12 12" fill="none" stroke="#fff" stroke-width="4"/></svg>
  <div class="team">
    <div class="member"><div class="portrait"><div role="img" aria-label="Portrait photo of Bram Hestridge"></div></div><h3>Bram Hestridge</h3><p>Founder &amp; CEO</p><div class="social"><svg width="14" height="10" viewBox="0 0 14 10"><rect width="14" height="10" fill="#fff"/><path d="M0 0l7 6 7-6" fill="none" stroke="#1ba8c4"/></svg><i></i><i></i><i></i></div></div>
    <div class="member"><div class="portrait"><div role="img" aria-label="Portrait photo of Dorian Crestwell"></div></div><h3>Dorian Crestwell</h3><p>Co-Founder &amp; CFO</p><div class="social"><svg width="14" height="10" viewBox="0 0 14 10"><rect width="14" height="10" fill="#fff"/><path d="M0 0l7 6 7-6" fill="none" stroke="#1ba8c4"/></svg><i></i><i></i><i></i></div></div>
    <div class="member"><div class="portrait"><div role="img" aria-label="Portrait photo of Clara Dunmore"></div></div><h3>Clara Dunmore</h3><p>COO</p><div class="social"><svg width="14" height="10" viewBox="0 0 14 10"><rect width="14" height="10" fill="#fff"/><path d="M0 0l7 6 7-6" fill="none" stroke="#1ba8c4"/></svg><i></i><i></i><i></i></div></div>
    <div class="member"><div class="portrait"><div role="img" aria-label="Portrait photo of Naomi Castell"></div></div><h3>Naomi Castell</h3><p>CTO</p><div class="social"><svg width="14" height="10" viewBox="0 0 14 10"><rect width="14" height="10" fill="#fff"/><path d="M0 0l7 6 7-6" fill="none" stroke="#1ba8c4"/></svg><i></i><i></i><i></i></div></div>
  </div>
</section>

<section class="services">
  <h2 class="sec-title"><span class="rule"></span><span class="mark"></span><span style="color:var(--green)">SERVICES</span><span class="rule"></span></h2>
  <div class="service one">
    <div class="icon"><svg width="60" height="56" viewBox="0 0 60 56"><circle cx="20" cy="18" r="8" fill="var(--teal)"/><path d="M6 48c0-12 6-18 14-18s14 6 14 18z" fill="var(--teal)"/><rect x="32" y="4" width="24" height="22" fill="none" stroke="var(--teal)" stroke-width="3"/><path d="M38 20v-7l6-5 6 5v7z" fill="var(--teal)"/></svg></div>
    <div class="body">
      <h3>Property Investment Consulting</h3>
      <p>Lorem ipsum dolor sit amet, consectetuer adipiscing elit, sed diam nonummy nibh euismod tincidunt ut laoreet dolore magna aliquam erat volutpat. Ut wisi enim ad minim veniam, quis nostrud exerci tation ullamcorper suscipit lobortis nisl ut aliquip ex ea commodo.</p>
      <span class="btn">LEARN MORE</span>
    </div>
  </div>
  <div class="service two">
    <div class="icon"><svg width="56" height="56" viewBox="0 0 56 56"><rect x="12" y="6" width="32" height="44" fill="var(--teal)"/><rect x="4" y="22" width="10" height="28" fill="var(--teal)"/><rect x="42" y="22" width="10" height="28" fill="var(--teal)"/><g fill="#fff"><rect x="17" y="12" width="6" height="6"/><rect x="25" y="12" width="6" height="6"/><rect x="33" y="12" width="6" height="6"/><rect x="17" y="22" width="6" height="6"/><rect x="25" y="22" width="6" height="6"/><rect x="33" y="22" width="6" height="6"/><rect x="17" y="32" width="6" height="6"/><rect x="33" y="32" width="6" height="6"/><rect x="25" y="38" width="6" height="12"/></g></svg></div>
    <div class="body">
      <h3>Sales of Apartment Properties</h3>
      <p>Lorem ipsum dolor sit amet, consectetuer adipiscing elit, sed diam nonummy nibh euismod tincidunt ut laoreet dolore magna aliquam erat volutpat. Ut wisi enim ad minim veniam, quis nostrud exerci tation ullamcorper suscipit lobortis nisl ut aliquip ex ea commodo.</p>
      <span class="btn">LEARN MORE</span>
    </div>
  </div>
</section>

<section class="approach on-teal" role="group" aria-label="Our approach">
  <svg width="1200" height="498" viewBox="0 0 1200 498" aria-hidden="true">
    <path d="M214 280a158 158 0 0 0 316 0h-36a122 122 0 0 1-244 0z" fill="var(--slate)"/>
    <path d="M670 280a158 158 0 0 0 316 0h-36a122 122 0 0 1-244 0z" fill="var(--slate)"/>
    <path d="M442 280a158 158 0 0 1 316 0h-36a122 122 0 0 0-244 0z" fill="var(--green)"/>
    <circle cx="372" cy="280" r="118" fill="#fff"/>
    <circle cx="828" cy="280" r="118" fill="#fff"/>
    <circle cx="600" cy="280" r="118" fill="#fff"/>
  </svg>
  <h2 class="sec-title" style="position:relative"><span class="rule"></span><span class="mark"></span><span>OUR APPROACH</span><span class="rule"></span></h2>
  <div class="step" style="left:287px;top:262px;width:170px"><h3>CONSULTING</h3><p>Clients approach us with their investment goals</p></div>
  <div class="step" style="left:512px;top:205px;width:176px"><h3>OUR EXPERTISE</h3><p>We have a team of researchers, transaction coordinators and marketing personal to support our geographically specialized advisers.</p></div>
  <div class="step" style="left:743px;top:230px;width:170px"><h3>REACH GOALS</h3><p>We present the ideal solutions and unique way of better helping clients achieving their investment goals.</p></div>
</section>

<section class="testimonials">
  <h2 class="sec-title"><span class="rule"></span><span class="mark"></span><span>WHAT CLIENTS <em>SAY</em></span><span class="rule"></span></h2>
  <div class="quote">
    <span class="q open">&ldquo;</span>
    Lorem ipsum dolor sit amet, consectetuer adipiscing elit, sed diam nonummy nibh euismod tincidunt ut laoreet dolore magna aliquam erat volutpat. Ut wisi enim ad minim veniam, quis nostrud exercitation ullamcorper suscipit lobortis nisl ut aliquip ex ea commodo conse quat. Duis autem vel eum iriure dolor in hendrerit in vulputate velit esse.<span class="close">&rdquo;</span>
    <span class="tail"></span>
  </div>
  <div class="author">Stuart Calloway</div>
  <div class="dots"><i class="on"></i><i></i><i></i><i></i></div>
</section>

<footer class="footer">
  <div class="brand"><div class="mark"></div><div class="name">MERIDIAN ADVISERS</div></div>
  <div class="fcol" style="left:123px"><h4>QUICK LINKS</h4><ul><li>Home</li><li>About</li><li>Our People</li><li>Services</li><li>Approach</li><li>Testimonials</li><li>Contact</li></ul></div>
  <div class="fcol" style="left:298px"><h4>SERVICES</h4><ul><li>Property Investment Consulting</li><li>Sale of Apartment Properties</li></ul></div>
  <div class="fcol" style="left:558px">
    <h4>CONTACT</h4>
    <div class="line"><svg width="16" height="16" viewBox="0 0 16 16"><circle cx="8" cy="8" r="7.5" fill="none" stroke="var(--ink)"/><path d="M8 3.5a3 3 0 0 0-3 3c0 2.5 3 6 3 6s3-3.5 3-6a3 3 0 0 0-3-3z" fill="var(--ink)"/></svg><span>Meridian Advisers<br>450 Harbor View Dr<br>Suite #210<br>Los Angeles, CA 90017</span></div>
    <div class="line"><svg width="16" height="16" viewBox="0 0 16 16"><circle cx="8" cy="8" r="7.5" fill="none" stroke="var(--ink)"/><path d="M5.5 4l1.5 1.5-.7 1a5 5 0 0 0 2.7 2.7l1-.7L11.5 10l-1 1.5C7 11.5 4.5 9 4.5 5.5z" fill="var(--ink)"/></svg><span>+1 (555) 014 2290</span></div>
    <div class="line"><svg width="16" height="16" viewBox="0 0 16 16"><circle cx="8" cy="8" r="7.5" fill="none" stroke="var(--ink)"/><rect x="4" y="5" width="8" height="6" fill="none" stroke="var(--ink)"/><path d="M4 5l4 3 4-3" fill="none" stroke="var(--ink)"/></svg><span>hello@meridianadvisers.example</span></div>
  </div>
  <div class="fcol" style="left:821px">
    <h4 style="width:261px">NEWSLETTER SIGN UP</h4>
    <div class="signup"><div class="field">Enter Email Address</div><div class="go">SIGN UP</div></div>
  </div>
</footer>
<div class="copyright">© COPYRIGHT 2017 MERIDIAN ADVISERS. ALL RIGHTS RESERVED</div>

</body>
</html>
```